Bella Farina Restaurants - New Menu Design

We need a new look for the menu to keep things fresh and customers returning regularly.

Bella Farina (bel*la fareena), "The Pretty Flour", is a Cantina style restaurant & bar concept born by locals Ronny Castell and Dale Morrow in 2012.
The Cantina in Italy brings back fond memories as it is best known as a neighborhood tavern that is warm and cheerful, patronized by local and steady clientele.

We offer a Neapolitan inspired menu of made-from-scratch dishes that represent traditional Italian cuisine. These meals pay homage to the memories of Campania, the region of our heritage. The dishes are typical to the working-class neighborhoods of Napoli, Salerno, Capri and the dozens of small villages along the prized Amalfi Coast.

Bella Farina has three locations: Vienna, VA, Ashburn, VA and Clarksburg, MD.

Target Market(s)

Local, affluent families which we already do a very good job of attracting and keeping as regular customers, but we can always handle more.

Industry/Entity Type

Restaurant

Requirements
Must have
• Style of logo “type/letters” should stay the same, color scheme can definitely be changed. We also want to emphasize “Authentic Italian Food”. To put it simply, we are looking for a more sophisticated look.
• The menu is currently a tri-fold with print on both sides. 11” height by 17-1/4” wide, each trifold section is 11” high by 5-3/4” wide.

```html
<!DOCTYPE html>
<html lang="en">
<head>
<meta charset="utf-8">
<title>Bella Farina – Menu</title>
<link rel="stylesheet" href="https://fonts.googleapis.com/css2?family=Libre+Baskerville&family=Source+Sans+3:wght@400;600&display=swap">
<style>
  :root {
    --green: #00914b;
    --orange: #f0932f;
    --blue: #2f4c9c;
    --navy: #24507e;
    --red: #e3232b;
    --ink: #2f4c9c;
    --muted: #7a7a7a;
    --paper: #ffffff;
    --edge: #dcdcdc;
    --dark: #222222;
  }
  * { box-sizing: border-box; margin: 0; padding: 0; }
  html, body { width: 1200px; height: 1200px; overflow: hidden; background: var(--paper); }
  body { position: relative; font-family: "Source Sans 3", Arial, sans-serif; }

  .panel { position: absolute; top: 98px; width: 466px; background: var(--paper); border: 1px solid var(--edge); overflow: hidden; }
  .cover { left: 94px; height: 999px; }
  .menu-page { left: 640px; height: 960px; }

  .color-band { position: absolute; left: 0; right: 0; height: 51px; display: flex; }
  .color-band span { flex: 1; }
  .color-band.top { top: 0; }
  .color-band.bottom { bottom: 0; }
  .c-green { background: var(--green); }
  .c-orange { background: var(--orange); }
  .c-blue { background: var(--blue); }
  .c-red { background: var(--red); }
  .c-navy { background: var(--navy); }

  .brand-name { position: absolute; left: 0; right: 0; top: 468px; text-align: center; font-weight: 600; font-size: 54px; line-height: 60px; color: var(--red); letter-spacing: 0.5px; }
  .tagline { position: absolute; left: 0; right: 0; top: 532px; text-align: center; font-family: "Libre Baskerville", Georgia, serif; font-size: 23px; line-height: 30px; color: var(--dark); }

  .side-stripe { position: absolute; left: 0; top: 0; bottom: 0; width: 38px; display: flex; flex-direction: column; }
  .side-stripe span { flex: 1; }

  .section-title { position: absolute; left: 68px; font-family: "Libre Baskerville", Georgia, serif; font-size: 21px; line-height: 26px; font-weight: 400; color: var(--orange); }
  .section-title.appetizers { top: 48px; }
  .section-title.salads { top: 536px; }
  .section-title .it-red { color: var(--red); }

  .dish { position: absolute; left: 68px; right: 43px; }
  .dish-name { font-size: 12px; color: var(--ink); line-height: 15px; }
  .dish-desc { font-size: 8.5px; color: var(--muted); line-height: 11px; margin-top: 1px; max-width: 290px; }
  .dish-price { position: absolute; right: 0; top: 0; font-size: 11.5px; line-height: 15px; color: var(--ink); }

  .allergy-note { position: absolute; left: 68px; right: 43px; top: 918px; font-size: 7.5px; line-height: 10px; color: var(--muted); }
</style>
</head>
<body>

<section class="panel cover">
  <div class="color-band top"><span class="c-green"></span><span class="c-orange"></span><span class="c-blue"></span><span class="c-red"></span><span class="c-green"></span></div>
  <div class="brand-name">Bella Farina</div>
  <div class="tagline">Authentic Italian Food</div>
  <div class="color-band bottom"><span class="c-green"></span><span class="c-red"></span><span class="c-blue"></span><span class="c-orange"></span><span class="c-green"></span></div>
</section>

<section class="panel menu-page">
  <div class="side-stripe">
    <span class="c-green"></span><span class="c-orange"></span><span class="c-blue"></span><span class="c-red"></span>
    <span class="c-green"></span><span class="c-orange"></span><span class="c-blue"></span><span class="c-red"></span>
    <span class="c-green"></span><span class="c-orange"></span><span class="c-navy"></span><span class="c-red"></span>
    <span class="c-green"></span><span class="c-orange"></span><span class="c-navy"></span>
  </div>

  <h2 class="section-title appetizers">Sfizi Appetizers</h2>

  <div class="dish" style="top:87px"><div class="dish-name">Tuscan style flatbread</div><div class="dish-price">$6.00</div></div>
  <div class="dish" style="top:116px"><div class="dish-name">Bocconcini di salsiccia</div><div class="dish-desc">Sausage bites with parmesan cheese, onions and marinara sauce</div><div class="dish-price">$8.00</div></div>
  <div class="dish" style="top:158px"><div class="dish-name">Arancini</div><div class="dish-desc">Saffron risotto balls filled with caciocavallo cheese,<br>mozzarella, peas &amp; meat sauce</div><div class="dish-price">$8.00</div></div>
  <div class="dish" style="top:210px"><div class="dish-name">Mozzarella in Carrozza</div><div class="dish-desc">Panfried buffalo mozzarella with garlic anchovy sauce<br>or spicy tomato sauce</div><div class="dish-price">$8.00</div></div>
  <div class="dish" style="top:263px"><div class="dish-name">Cozze alla Napoletana*</div><div class="dish-desc">Fried calamari with spicy tomato sauce, or grilled with arugula</div><div class="dish-price">$8.00</div></div>
  <div class="dish" style="top:306px"><div class="dish-name">Calamari fritti o alla griglia*</div><div class="dish-desc">Fried calamari with spicy tomato sauce, or grilled with arugula</div><div class="dish-price">$11.00</div></div>
  <div class="dish" style="top:349px"><div class="dish-name">Zuchini alla scapece</div><div class="dish-desc">Grilled zuchini with garlic EVOO, mint, and red wine vinegar</div><div class="dish-price">$8.00</div></div>
  <div class="dish" style="top:391px"><div class="dish-name">Tortina rustico Napoletano</div><div class="dish-desc">Puff pastry stuffed with ricotta, smoked mozzarella,<br>parmesan cheese and cured meat</div><div class="dish-price">$12.00</div></div>
  <div class="dish" style="top:445px"><div class="dish-name">Pomodoro ripieni</div><div class="dish-desc">Stuffed tomato with saffron risotto, ground trio of meat<br>mozzarella and peas</div><div class="dish-price">$9.00</div></div>

  <h2 class="section-title salads"><span class="it-red">Insalatiera</span> Salad lady</h2>

  <div class="dish" style="top:578px"><div class="dish-name">Insalata Di Cesare*</div><div class="dish-desc">Mixed Greens With Balsamic Vinaigrette Dressing</div><div class="dish-price">$8.00</div></div>
  <div class="dish" style="top:619px"><div class="dish-name">Insalata Della Casa</div><div class="dish-desc">Mixed Greens With Balsamic Vinaigrette Dressing</div><div class="dish-price">$6.00</div></div>
  <div class="dish" style="top:661px"><div class="dish-name">Insalata Caprese</div><div class="dish-desc">Fresh Mozzarella, Vine Ripe Tomatoes, Fresh Basil, &amp; Extra Virgin Olive Oil<br>With Balsamic Reduction</div><div class="dish-price">$8.00</div></div>
  <div class="dish" style="top:721px"><div class="dish-name">Insalata Bella Farina</div><div class="dish-desc">Boston Bibb Chopped Salad With Eggs, Avocado, Sliced Tomatoes, Olives,<br>Sweet Onions &amp; Mozzarella Cheese With Balsamic Vinaigrette</div><div class="dish-price">$14.00</div></div>
  <div class="dish" style="top:777px"><div class="dish-name">Tritato</div><div class="dish-desc">Chopped Salad, Tomato, Onion, Lettuce, Speck, Baby Shrimp In A Tangy Bleu<br>Cheese Dressing Topped With A Crusted Shrimp &amp; Crumbled Bleu Cheese</div><div class="dish-price">$12.00</div></div>
  <div class="dish" style="top:835px"><div class="dish-name">Insalata Di Bietole</div><div class="dish-desc">Beets, Goat Cheese, Baby Arugula With A Balsamic Vinaigrette</div><div class="dish-price">$9.00</div></div>

  <p class="allergy-note">*May contain raw or undercooked ingredients. Consuming raw or undercooked meats, poultry, seafood, shellfish, or eggs may increase your risk of foodborne illness, especially if you have certain medical conditions. Please notify your server if you have food allergies.</p>
</section>

</body>
</html>
```